Release Therapy business card that deals with the release of negative issues

I need a business card for my business called PEBBLES (A warm hearth to rest when you tire) ... I'm a therapist that deals with people releasing negative issues, by applying therapies that incorporate, hypnosis, aromatherapy and listen therapy..I like the colour green and soft blues...My idea is for a hand releasing butterflies, and incorporating soft clouds....
Target Market(s)
All people, all ages
Industry/Entity Type
Business
Contact Information for Business Card
PEBBLES"A Warm Hearth To Rest When You Tire"Yvette R BrockingtonRelease Therapist0411 743 781email: calmingpaths4you@quietmail.example
Requirements
Must have
- butterflies and soft clouds
Nice to have
- I like the decorative and script fonts for business name, and also my name
- Marisol T Fenwhistle...

```html
<!DOCTYPE html>
<html lang="en">
<head>
<meta charset="utf-8">
<title>PEBBLES – Release Therapist Business Cards</title>
<link rel="stylesheet" href="https://fonts.googleapis.com/css2?family=Great+Vibes&family=Montserrat:wght@400;500&display=swap">
<style>
  :root {
    --backdrop: #e9e9ea;
    --card-base: #eef6f6;
    --sky-blue: #bfe3ee;
    --sky-mint: #d8efe6;
    --sky-pale: #f4f8f3;
    --teal: #2fa9bd;
    --teal-deep: #1f7f95;
    --leaf-green: #8cc43f;
    --frame-line: #9fd6df;
    --paper-white: #ffffff;
    --butterfly-tint: rgba(170, 214, 160, 0.7);
    --hand-tint: rgba(130, 196, 214, 0.6);
  }
  * { box-sizing: border-box; margin: 0; padding: 0; }
  html, body {
    width: 1200px;
    height: 848px;
    overflow: hidden;
    background: var(--backdrop);
    font-family: "Montserrat", Arial, sans-serif;
  }
  .stage { position: relative; width: 1200px; height: 848px; }

  .card {
    position: absolute;
    width: 540px;
    height: 308px;
    border-radius: 3px;
    overflow: hidden;
    background: var(--card-base);
    box-shadow: 0 6px 18px rgba(0, 0, 0, 0.12);
  }
  .card--front { left: 210px; top: 80px; }
  .card--back  { left: 450px; top: 450px; }

  .watercolour-sky {
    position: absolute;
    inset: 0;
    background:
      radial-gradient(ellipse 60% 45% at 25% 20%, var(--sky-blue) 0%, transparent 70%),
      radial-gradient(ellipse 55% 50% at 80% 30%, var(--sky-blue) 0%, transparent 75%),
      radial-gradient(ellipse 70% 40% at 50% 85%, var(--sky-mint) 0%, transparent 75%),
      linear-gradient(180deg, #cfe9f1 0%, var(--sky-pale) 60%, #e3f2ea 100%);
  }

  .brand {
    position: absolute;
    display: flex;
    flex-direction: column;
    align-items: flex-start;
  }
  .brand__row { display: flex; align-items: center; gap: 10px; }
  .brand__dot {
    width: 18px; height: 18px;
    border-radius: 50%;
    background: var(--teal);
  }
  .brand__name {
    color: var(--teal);
    font-weight: 500;
    letter-spacing: 0.18em;
  }
  .brand__tagline {
    color: var(--teal-deep);
    font-weight: 400;
    letter-spacing: 0.02em;
    margin-top: 4px;
  }

  /* Front card */
  .card--front .brand { left: 120px; top: 46px; }
  .card--front .brand__name { font-size: 38px; }
  .card--front .brand__tagline { font-size: 12.5px; }

  .appointment__label {
    position: absolute;
    left: 0; right: 0;
    top: 168px;
    text-align: center;
    color: var(--leaf-green);
    font-size: 13px;
    letter-spacing: 0.03em;
  }
  .appointment__box {
    position: absolute;
    left: 56px;
    right: 56px;
    top: 198px;
    height: 74px;
    background: var(--paper-white);
    border: 1.5px solid var(--frame-line);
  }

  /* Back card */
  .card--back .brand { left: 34px; top: 30px; }
  .card--back .brand__dot { width: 12px; height: 12px; }
  .card--back .brand__name { font-size: 24px; }
  .card--back .brand__tagline { font-size: 8.5px; }

  .release-artwork {
    position: absolute;
    right: 0;
    top: 0;
    width: 250px;
    height: 240px;
    background:
      radial-gradient(ellipse 55% 45% at 50% 35%, var(--butterfly-tint) 0%, transparent 75%),
      radial-gradient(ellipse 70% 35% at 55% 85%, var(--hand-tint) 0%, transparent 80%);
  }

  .person { position: absolute; left: 34px; top: 140px; }
  .person__name {
    font-family: "Great Vibes", cursive;
    color: var(--teal-deep);
    font-size: 38px;
    line-height: 1;
  }
  .person__role {
    color: var(--leaf-green);
    font-size: 16px;
    margin-top: 2px;
    margin-left: 22px;
  }

  .contact {
    position: absolute;
    left: 34px;
    bottom: 28px;
    color: var(--teal);
    font-size: 16px;
    line-height: 1.45;
    font-style: normal;
  }
</style>
</head>
<body>
  <main class="stage">

    <section class="card card--front" aria-label="Appointment card">
      <div class="watercolour-sky" role="img" aria-label="Soft watercolour sky in pale blues and mint greens"></div>
      <div class="brand">
        <div class="brand__row">
          <span class="brand__dot"></span>
          <span class="brand__name">PEBBLES</span>
        </div>
        <p class="brand__tagline">A Warm Hearth To Rest When You Tire</p>
      </div>
      <p class="appointment__label">Next Appointment</p>
      <div class="appointment__box"></div>
    </section>

    <section class="card card--back" aria-label="Contact card">
      <div class="watercolour-sky" role="img" aria-label="Soft watercolour sky in pale blues and mint greens"></div>
      <div class="release-artwork" role="img" aria-label="Faint open hand releasing pale green butterflies above soft pebbles"></div>
      <div class="brand">
        <div class="brand__row">
          <span class="brand__dot"></span>
          <span class="brand__name">PEBBLES</span>
        </div>
        <p class="brand__tagline">A Warm Hearth To Rest When You Tire</p>
      </div>
      <div class="person">
        <p class="person__name">Marisol T Fenwhistle</p>
        <p class="person__role">Release Therapist</p>
      </div>
      <address class="contact">
        <div class="contact__phone">0482 516 904</div>
        <div class="contact__email">calmingpaths4you@quietmail.example</div>
      </address>
    </section>

  </main>
</body>
</html>
```